Varnel Solutions requires a new business card.

We are an online professional tool store.

Target Market(s)

We target the professional technician.

Industry/Entity Type

Business

Contact Information for Business Card

VarnelSolutions.com.au

sales@varnelsolutions.com

Requirements
Must have
• Needs to look commercial and professional
Should not have
• No Australian Colors, maps or shapes.
• No Shapes of Tools

```html
<!DOCTYPE html>
<html lang="en">
<head>
<meta charset="utf-8">
<title>Varnel Solutions — Business Card</title>
<link rel="stylesheet" href="https://fonts.googleapis.com/css2?family=Open+Sans:wght@400;600&display=swap">
<style>
  :root {
    --backdrop: #3a3633;
    --card: #0d0d0e;
    --brand-blue: #1d3fd8;
    --accent-cyan: #1e9fd8;
    --text-light: #e8e8e8;
    --text-muted: #cfcfcf;
    --divider: #3b3b3e;
  }
  * { box-sizing: border-box; margin: 0; padding: 0; }
  html, body {
    width: 1200px;
    height: 844px;
    overflow: hidden;
    background: var(--backdrop);
    font-family: "Open Sans", Arial, sans-serif;
  }
  .stage {
    position: relative;
    width: 1200px;
    height: 844px;
  }
  .card {
    position: absolute;
    top: 272px;
    width: 525px;
    height: 300px;
    background: var(--card);
    border-radius: 3px;
    box-shadow: 0 10px 30px rgba(0,0,0,0.45);
  }
  .card--front { left: 50px; }
  .card--back { left: 625px; }

  .brand {
    position: absolute;
    display: flex;
    align-items: center;
    gap: 10px;
    color: var(--brand-blue);
    font-weight: 600;
    white-space: nowrap;
  }
  .brand__dot {
    border-radius: 50%;
    background: var(--brand-blue);
  }
  .card--front .brand { left: 70px; top: 62px; font-size: 30px; }
  .card--front .brand__dot { width: 20px; height: 20px; }
  .card--back .brand {
    left: 0; right: 0; top: 125px;
    justify-content: center;
    font-size: 38px;
  }
  .card--back .brand__dot { width: 26px; height: 26px; }

  .identity {
    position: absolute;
    right: 250px;
    top: 168px;
    text-align: right;
    white-space: nowrap;
  }
  .identity__name {
    color: var(--accent-cyan);
    font-size: 22px;
    font-weight: 600;
    line-height: 1.2;
  }
  .identity__role {
    color: var(--text-muted);
    font-size: 14px;
    margin-bottom: 14px;
  }
  .identity__address {
    color: var(--text-light);
    font-size: 15px;
    line-height: 1.3;
  }

  .divider {
    position: absolute;
    left: 292px;
    top: 150px;
    width: 1px;
    height: 110px;
    background: var(--divider);
  }

  .contact {
    position: absolute;
    left: 310px;
    top: 152px;
    list-style: none;
  }
  .contact__item {
    display: flex;
    align-items: center;
    gap: 10px;
    color: var(--text-light);
    font-size: 13.5px;
    height: 24px;
    white-space: nowrap;
  }
  .contact__icon {
    width: 11px;
    height: 11px;
    fill: var(--accent-cyan);
    flex: none;
  }
</style>
</head>
<body>
<main class="stage">
  <section class="card card--front" aria-label="Business card front">
    <div class="brand">
      <span class="brand__dot"></span>
      <span class="brand__name">Varnel Solutions</span>
    </div>

    <div class="identity">
      <p class="identity__name">Daniel Hartley</p>
      <p class="identity__role">Managing Director</p>
      <p class="identity__address">12345, Address Goes Here<br>Country Name, 123456</p>
    </div>

    <div class="divider"></div>

    <ul class="contact">
      <li class="contact__item">
        <svg class="contact__icon" viewBox="0 0 12 12" aria-hidden="true"><path d="M2.4 0.6 L4.2 2.8 L3.2 4.2 Q4.6 6.9 7.8 8.8 L9.2 7.8 L11.4 9.6 L10.2 11.4 Q4.8 11 0.6 1.8 Z"/></svg>
        <span>(044)-555-0187</span>
      </li>
      <li class="contact__item">
        <svg class="contact__icon" viewBox="0 0 12 12" aria-hidden="true"><path d="M3 0 H9 V3 H3 Z M0 4 H12 V9 H10 V7 H2 V9 H0 Z M3 8 H9 V12 H3 Z"/></svg>
        <span>555-014-2290</span>
      </li>
      <li class="contact__item">
        <svg class="contact__icon" viewBox="0 0 12 12" aria-hidden="true"><path d="M0 2 H12 V10 H0 Z" /><path d="M0.6 2.6 L6 6.6 L11.4 2.6" stroke="#0d0d0e" stroke-width="1.2" fill="none"/></svg>
        <span>sales@varnelsolutions.com</span>
      </li>
      <li class="contact__item">
        <svg class="contact__icon" viewBox="0 0 12 12" aria-hidden="true"><circle cx="6" cy="6" r="6"/><path d="M0 6 H12 M6 0 Q2.5 6 6 12 M6 0 Q9.5 6 6 12" stroke="#0d0d0e" stroke-width="0.9" fill="none"/></svg>
        <span>VarnelSolutions.com.au</span>
      </li>
    </ul>
  </section>

  <section class="card card--back" aria-label="Business card back">
    <div class="brand">
      <span class="brand__dot"></span>
      <span class="brand__name">Varnel Solutions</span>
    </div>
  </section>
</main>
</body>
</html>
```